SkyVelour IOS App for iPhone / Luxury private aviation / 1 main screen

Hello there !

SkyVelour Ltd is a VIP aircraft operator. You can see our https://facebook.example/skyvelour page or our https://instagram.example/sky_velour . Our web page http://skyvelour.example says it all, we don't communicate much except for the music industry activities we have.

We have developed a very simple app, 6 screens total, that will give the user a distance and a flight time between any two airports of the world. Enter a departure point (New York or JFK or KJFK...) and a destination (like Los Angeles, LAX or KLAX) and we will give you the flight time depending on the type of private jet you are selecting in the aircraft database of the app.

You might want to see the attached pdf for the flow...Any design idea is welcome.

We want it to be simple, pure, fast, and of course less will be more. We should see a unity between all these screens, same design spirit of course... On the main screen of the app, we are showing:- the company logo- a departure airport- a destination airport- the selected aircraft with access to a mini photo gallery of the said airplane- a flight time shown in hours and minutes- a distance shown in Miles, Nautical Miles or KM according to the pref page selection- an access to a contact screen- an access to a parameters screen (will develop some of it on a later version).

Thanks !!

Mathis

Target Market(s)

Private aircraft travelers and VIP flights brokers

Industry/Entity Type

Aviation

Font styles to use
Sans Serif

Colors
aaaaaa
5c5c5c
1b1b1b
e9e9e9
ffffff

Requirements
Must have
• Our logo
Nice to have
• Elegant design
Should not have
• Complicated stuff

```html
<!DOCTYPE html>
<html lang="en">
<head>
<meta charset="utf-8">
<title>SkyVelour – Flight</title>
<link rel="stylesheet" href="https://fonts.googleapis.com/css2?family=Roboto:wght@300;400;500;700&display=swap">
<style>
  :root {
    --sky: #38aeea;
    --ink: #1b1b1b;
    --text: #5c5c5c;
    --muted: #aaaaaa;
    --mist: #e9e9e9;
    --panel: #f1f1f1;
    --white: #ffffff;
    --amber: #f2a23a;
  }
  * { margin: 0; padding: 0; box-sizing: border-box; }
  html, body { width: 1200px; height: 2268px; overflow: hidden; }
  body {
    position: relative;
    background: var(--mist);
    font-family: "Roboto", sans-serif;
    color: var(--text);
  }
  .abs { position: absolute; }

  /* Top bar */
  .app-bar { left: 0; top: 0; width: 1200px; height: 320px; background: var(--sky); }
  .menu-icon { left: 64px; top: 176px; }
  .bell-icon { left: 1082px; top: 168px; }
  .brand {
    left: 0; width: 1200px; top: 196px; text-align: center;
    color: var(--white); font-weight: 400; font-size: 30px; letter-spacing: 10px;
  }

  /* Flight card */
  .card { left: 72px; top: 416px; width: 1056px; height: 1432px; background: var(--white);
    box-shadow: 0 2px 8px rgba(0,0,0,0.12); border-radius: 6px; overflow: hidden; }
  .route-banner { left: 0; top: 0; width: 1056px; height: 248px;
    background: linear-gradient(180deg, #3b4450 0%, #1f242c 55%, #2b2f35 100%); }
  .code { top: 56px; color: var(--white); font-weight: 700; font-size: 88px; line-height: 1; text-align: center; }
  .city { top: 150px; color: var(--white); font-size: 24px; text-align: center; }
  .from { left: 100px; width: 200px; }
  .to { left: 720px; width: 260px; }
  .banner-plane { left: 492px; top: 88px; }

  .schedule { left: 0; top: 248px; width: 1056px; height: 496px; }
  .label-small { font-size: 20px; letter-spacing: 1px; color: var(--text); }
  .flight-label { left: 0; width: 1056px; top: 62px; text-align: center; }
  .flight-no { left: 0; width: 1056px; top: 92px; text-align: center; font-size: 30px; color: var(--ink); }
  .leg { width: 300px; text-align: center; }
  .leg-dep { left: 50px; }
  .leg-arr { left: 676px; }
  .leg-icon { top: 68px; left: 116px; }
  .date { top: 188px; width: 300px; font-size: 26px; color: var(--text); }
  .time { top: 252px; width: 300px; font-size: 64px; font-weight: 300; color: var(--text); }
  .airport { top: 340px; width: 300px; font-size: 24px; line-height: 34px; color: var(--muted); }
  .duration { left: 328px; width: 400px; top: 222px; text-align: center; font-size: 28px; color: var(--text); }
  .duration-line { left: 352px; top: 266px; width: 352px; height: 6px; background: var(--sky); }
  .nonstop { left: 328px; width: 400px; top: 290px; text-align: center; font-size: 28px; color: var(--text); }

  .details { left: 0; top: 744px; width: 1056px; height: 568px; background: var(--panel);
    border-top: 3px dashed #d2d2d2; }
  .field-label { font-size: 22px; color: var(--muted); letter-spacing: 1px; }
  .field-value { font-size: 26px; color: var(--text); font-weight: 500; }
  .col-a { left: 184px; }
  .col-b { left: 660px; }
  .social { top: 356px; }
  .social-a { left: 664px; }
  .social-b { left: 780px; }

  .contact { left: 0; top: 1312px; width: 1056px; height: 120px; background: var(--sky);
    color: var(--white); font-size: 38px; font-weight: 500; text-align: center; line-height: 120px; }

  /* Distance strip */
  .distance-strip { left: 0; top: 1940px; width: 1200px; height: 328px; background: var(--ink); color: var(--white); }
  .gc-title { left: 0; width: 1200px; top: 44px; text-align: center; font-size: 30px; }
  .track-done { left: 280px; top: 154px; width: 220px; height: 4px; background: var(--amber); }
  .track-left { left: 500px; top: 154px; width: 436px; height: 4px; background: #6a6a6a; }
  .track-plane { left: 460px; top: 122px; }
  .km { font-size: 26px; line-height: 34px; color: var(--white); }
  .km-left { left: 96px; top: 130px; }
  .km-right { left: 950px; top: 130px; }
  .avg { left: 0; width: 1200px; top: 226px; text-align: center; font-size: 20px; color: var(--muted); }
</style>
</head>
<body>

<header class="abs app-bar">
  <svg class="abs menu-icon" width="60" height="48" viewBox="0 0 60 48" aria-label="Menu">
    <rect x="0" y="0" width="52" height="6" rx="3" fill="#fff"/>
    <rect x="0" y="20" width="40" height="6" rx="3" fill="#fff"/>
    <rect x="0" y="40" width="52" height="6" rx="3" fill="#fff"/>
  </svg>
  <div class="abs brand">SKYVELOUR</div>
  <svg class="abs bell-icon" width="52" height="60" viewBox="0 0 52 60" aria-label="Notifications">
    <path d="M26 4c-10 0-17 8-17 18v14L3 44v4h46v-4l-6-8V22C43 12 36 4 26 4z" fill="#fff"/>
    <circle cx="26" cy="54" r="6" fill="#fff"/>
  </svg>
</header>

<main class="abs card">
  <section class="abs route-banner" role="img" aria-label="Photograph of a London bridge at dusk">
    <div class="abs code from">BOS</div>
    <div class="abs city from">BOSTON</div>
    <svg class="abs banner-plane" width="72" height="72" viewBox="0 0 24 24" aria-hidden="true">
      <path d="M21 16v-2l-8-5V3.5a1.5 1.5 0 0 0-3 0V9l-8 5v2l8-2.5V19l-2 1.5V22l3.5-1 3.5 1v-1.5L13 19v-5.5z" fill="#fff" transform="rotate(90 12 12)"/>
    </svg>
    <div class="abs code to">LHR</div>
    <div class="abs city to">LONDON</div>
  </section>

  <section class="abs schedule">
    <div class="abs label-small flight-label">FLIGHT</div>
    <div class="abs flight-no">SV1325</div>

    <div class="abs leg leg-dep" style="top:0;height:496px;">
      <svg class="abs leg-icon" width="68" height="68" viewBox="0 0 24 24" aria-label="Departure">
        <path d="M21 16v-2l-8-5V3.5a1.5 1.5 0 0 0-3 0V9l-8 5v2l8-2.5V19l-2 1.5V22l3.5-1 3.5 1v-1.5L13 19v-5.5z" fill="#3a3a3a" transform="rotate(60 12 12)"/>
      </svg>
      <div class="abs date">Wed 2nd jan</div>
      <div class="abs time">08:25</div>
      <div class="abs airport">Boston International<br>Airport</div>
    </div>

    <div class="abs duration">15h 40m</div>
    <div class="abs duration-line"></div>
    <div class="abs nonstop">NON-STOP</div>

    <div class="abs leg leg-arr" style="top:0;height:496px;">
      <svg class="abs leg-icon" width="68" height="68" viewBox="0 0 24 24" aria-label="Arrival">
        <path d="M21 16v-2l-8-5V3.5a1.5 1.5 0 0 0-3 0V9l-8 5v2l8-2.5V19l-2 1.5V22l3.5-1 3.5 1v-1.5L13 19v-5.5z" fill="#3a3a3a" transform="rotate(125 12 12)"/>
      </svg>
      <div class="abs date">Wed 2nd jan</div>
      <div class="abs time">13:25</div>
      <div class="abs airport">London International<br>Airport</div>
    </div>
  </section>

  <section class="abs details">
    <div class="abs field-label col-a" style="top:70px;">AIRCRAFT</div>
    <div class="abs field-value col-a" style="top:118px;">VELARA V320</div>
    <div class="abs field-label col-b" style="top:70px;">CABIN</div>
    <div class="abs field-value col-b" style="top:118px;">GUEST PREMIUM</div>

    <div class="abs field-label col-a" style="top:196px;">OPERATED BY</div>
    <div class="abs field-value col-a" style="top:248px;">HARBORLINE AIR</div>
    <div class="abs field-label col-b" style="top:196px;">BOOKING NUMBER</div>
    <div class="abs field-value col-b" style="top:246px;">FB42X6</div>

    <div class="abs field-label col-a" style="top:350px;">PASSENGERS</div>
    <div class="abs field-value col-a" style="top:412px;">MR OSTROVEN DANIEL</div>

    <svg class="abs social social-a" width="80" height="80" viewBox="0 0 80 80" role="img" aria-label="Social page link">
      <circle cx="40" cy="40" r="38" fill="#3b5b9b"/>
    </svg>
    <svg class="abs social social-b" width="80" height="80" viewBox="0 0 80 80" role="img" aria-label="Photo feed link">
      <circle cx="40" cy="40" r="38" fill="#e0559b"/>
    </svg>
  </section>

  <div class="abs contact">CONTACT NOW</div>
</main>

<footer class="abs distance-strip">
  <div class="abs gc-title">GREAT CIRCLE DISTANCE: 1,540 KM</div>
  <div class="abs km km-left">444 KM<br>00:35 AGO</div>
  <div class="abs track-done"></div>
  <div class="abs track-left"></div>
  <svg class="abs track-plane" width="72" height="72" viewBox="0 0 24 24" aria-hidden="true">
    <path d="M21 16v-2l-8-5V3.5a1.5 1.5 0 0 0-3 0V9l-8 5v2l8-2.5V19l-2 1.5V22l3.5-1 3.5 1v-1.5L13 19v-5.5z" fill="#fff" transform="rotate(90 12 12)"/>
  </svg>
  <div class="abs km km-right">1,089 KM<br>IN 01:24</div>
  <div class="abs avg">ZQ1474 - AVERAGE FLIGHT TIME: 01:57</div>
</footer>

</body>
</html>
```